Yoga for Scoliosis business card/logo design

I need a business card/logo design for my new business. I am a registered yoga teacher and am certified in yoga for scoliosis. I'd like my card to read "Marlow Yoga Yoga for a Healthy Spine" and would like to incorporate one of the letters in my name{ ie the first vertical line of the letter " H "or "D"} to resemble a scoliotic spine. I regularly teach the following:Yoga for Scoliosis, Yoga for Back Health, Hatha yoga, Vinyasa yoga with Iyengar style alignment. This business is mostly for private clients, but I also teach group, semi-private & work shop classes. I like the colors green (light emerald) and royal blue. I'd like the design to be somewhat sleek, but not too modern. I also like the idea of a ying/yang symbol with a scoliotic spine dviding it.

Industry/Entity Type

Teacher

Contact Information for Business Card

Tamsin Marlow
200 RYT, Certified Yoga for Scoliosis Instructor
MarlowYoga.example
MarlowYoga@mailbox.example
415-629-3174

```html
<!DOCTYPE html>
<html lang="en">
<head>
<meta charset="utf-8">
<title>Marlow Yoga – Business Card</title>
<link href="https://fonts.googleapis.com/css2?family=Didact+Gothic&display=swap" rel="stylesheet">
<style>
  :root {
    --page-bg: #e9e6df;
    --card-dark: #16321a;
    --card-mid: #1f4a22;
    --leaf-light: #9fd43a;
    --leaf-mid: #5e9a25;
    --accent-orange: #e8743a;
    --text-soft: #c9d6c4;
    --icon-bg: #8cbf3a;
  }
  * { box-sizing: border-box; margin: 0; padding: 0; }
  html, body {
    width: 1200px; height: 1023px; overflow: hidden;
    background: var(--page-bg);
    font-family: "Didact Gothic", "Century Gothic", sans-serif;
  }
  .stage {
    width: 1200px; height: 1023px;
    display: flex; align-items: center; justify-content: center;
  }
  .business-card {
    position: relative;
    width: 1000px; height: 572px;
    background: linear-gradient(100deg, var(--card-dark) 0%, var(--card-mid) 45%, var(--card-dark) 100%);
    border-radius: 6px;
    overflow: hidden;
    box-shadow: 0 14px 40px rgba(0,0,0,.25);
  }
  .grass-photo {
    position: absolute; top: 0; right: 0;
    width: 520px; height: 100%;
    background:
      radial-gradient(ellipse at 45% 70%, rgba(200,235,120,.85) 0%, rgba(120,180,50,.6) 30%, rgba(40,90,30,0) 70%),
      linear-gradient(90deg, var(--card-mid) 0%, var(--leaf-mid) 40%, #3d7a22 80%, var(--card-dark) 100%);
  }
  .grass-photo::before {
    content: ""; position: absolute; inset: 0;
    background: linear-gradient(90deg, var(--card-mid) 0%, rgba(31,74,34,0) 35%);
  }
  .brand-block {
    position: absolute; left: 70px; top: 70px;
  }
  .brand-name {
    font-size: 82px; font-weight: 400; line-height: 1; color: var(--leaf-light);
    letter-spacing: 1px;
  }
  .tagline {
    margin-top: 14px;
    font-size: 26px; color: var(--accent-orange);
  }
  .contact-block {
    position: absolute; left: 70px; top: 300px;
  }
  .person-name { font-size: 38px; font-weight: 400; color: var(--leaf-light); }
  .person-title { margin-top: 8px; font-size: 22px; color: var(--text-soft); }
  .contact-list { margin-top: 26px; list-style: none; }
  .contact-list li {
    display: flex; align-items: center; gap: 14px;
    font-size: 24px; color: var(--text-soft); margin-bottom: 10px;
  }
  .contact-icon {
    width: 24px; height: 24px; border-radius: 3px;
    background: var(--icon-bg);
    display: flex; align-items: center; justify-content: center;
  }
</style>
</head>
<body>
<main class="stage">
  <section class="business-card">
    <div class="grass-photo" role="img" aria-label="Close-up photograph of green grass blades with water ripples"></div>

    <div class="brand-block">
      <h1 class="brand-name">Marlow Yoga</h1>
      <p class="tagline">Yoga for a Healthy Spine</p>
    </div>

    <div class="contact-block">
      <h2 class="person-name">Tamsin Marlow</h2>
      <p class="person-title">Certified Yoga for Scoliosis Instructor</p>
      <ul class="contact-list">
        <li>
          <span class="contact-icon">
            <svg width="16" height="16" viewBox="0 0 16 16"><path d="M4 2l2 3-1.5 1.5a8 8 0 0 0 5 5L11 10l3 2-1.5 2.5C7 14 2 9 1.5 3.5z" fill="#16321a"/></svg>
          </span>415-629-3174
        </li>
        <li>
          <span class="contact-icon">
            <svg width="16" height="16" viewBox="0 0 16 16"><circle cx="8" cy="8" r="6" fill="none" stroke="#16321a" stroke-width="1.5"/><path d="M2 8h12M8 2c-3 3-3 9 0 12M8 2c3 3 3 9 0 12" fill="none" stroke="#16321a" stroke-width="1.2"/></svg>
          </span>MarlowYoga.example
        </li>
        <li>
          <span class="contact-icon">
            <svg width="16" height="16" viewBox="0 0 16 16"><rect x="2" y="4" width="12" height="9" fill="none" stroke="#16321a" stroke-width="1.5"/><path d="M2 4l6 5 6-5" fill="none" stroke="#16321a" stroke-width="1.5"/></svg>
          </span>MarlowYoga@mailbox.example
        </li>
      </ul>
    </div>
  </section>
</main>
</body>
</html>
```